Designing a brochures for an educational counseling service provider

We would like a 4 sided design on a 11x8.5 paper, half folded. I have including a sample design we did to give you an idea of what we envision but we welcome creativity to make beautiful looking flyers. Text for the flier is included as well as our logo.
- The most important thing is capturing our audience/market. We will be handing these flies to schools, organizations and individual clients.

www.plorvaeducationalconsultants.example

Target Market(s)

We are targeting international students wanting to study in the U.S and Canada.

Industry/Entity Type

Education

Requirements
Must have
• - Clean and clear
• - Our logo should visible and well placed.
• - Could you the pictures of students, libraries and school buildings or you could use the pictures we already have.
Nice to have
• We would like this to match business cards.

```html
<!DOCTYPE html>
<html lang="en">
<head>
<meta charset="utf-8">
<title>Plorva International Educational Consultants – Brochure</title>
<link rel="stylesheet" href="https://fonts.googleapis.com/css2?family=Montserrat:wght@700;800;900&family=Open+Sans:wght@400;600;700&family=Fira+Sans:wght@600&display=swap">
<style>
  :root {
    --orange: #ee5a24;
    --charcoal: #3b3b3d;
    --ink: #2b2b2b;
    --navy: #1f3f8f;
    --white: #ffffff;
    --grey-light: #d9d9d9;
    --grey-mid: #9a9a9a;
  }
  * { box-sizing: border-box; margin: 0; padding: 0; }
  html, body { width: 777px; height: 1200px; overflow: hidden; background: var(--white); }
  .brochure { position: relative; width: 777px; height: 1200px; overflow: hidden; font-family: "Open Sans", sans-serif; color: var(--ink); }

  /* ---------- Outer spread ---------- */
  .cover-photo { position: absolute; left: 0; top: 0; width: 388px; height: 574px;
    background: radial-gradient(ellipse at 45% 35%, #ededed 0%, #c9c9c9 45%, #8e8e8e 100%); }
  .cover-shapes { position: absolute; left: 0; top: 0; }
  .icon-grid { position: absolute; left: 104px; top: 166px; width: 184px; height: 184px; }
  .icon-tile { position: absolute; width: 84px; height: 84px; border: 7px solid var(--orange); border-radius: 16px; background: var(--white); display: flex; align-items: center; justify-content: center; }
  .icon-tile svg { width: 46px; height: 46px; }

  .contact-card { position: absolute; left: 66px; top: 524px; display: flex; gap: 24px; align-items: flex-start; }
  .contact-card .phone-box { width: 38px; height: 38px; border: 3px solid var(--white); border-radius: 8px; display: flex; align-items: center; justify-content: center; margin-top: 2px; }
  .contact-card p { font-size: 7.2px; line-height: 9.4px; color: var(--white); }

  .brand { position: absolute; left: 440px; top: 56px; width: 290px; text-align: center; }
  .brand-dot { width: 60px; height: 60px; border-radius: 50%; background: var(--navy); margin: 0 auto 14px; }
  .brand-name { font-family: "Montserrat", sans-serif; font-weight: 800; color: var(--navy); font-size: 15px; line-height: 19px; text-transform: uppercase; letter-spacing: 0.5px; }

  .tagline { position: absolute; left: 400px; top: 254px; width: 380px; font-family: "Montserrat", sans-serif; font-weight: 800; font-style: normal; font-size: 9.4px; color: var(--white); letter-spacing: 0.3px; transform: rotate(-10.8deg); transform-origin: left center; white-space: nowrap; }

  .service-list { position: absolute; left: 482px; top: 335px; list-style: none; }
  .service-list li { display: flex; align-items: center; height: 44px; margin-bottom: 6.6px; }
  .service-list .mini-tile { width: 44px; height: 44px; border: 3px solid var(--white); border-radius: 9px; display: flex; align-items: center; justify-content: center; margin-right: 10px; }
  .service-list .mini-tile svg { width: 24px; height: 24px; }
  .service-list span { font-family: "Fira Sans", sans-serif; font-weight: 600; font-size: 17.5px; color: var(--white); letter-spacing: 0.3px; }

  .info-bar { position: absolute; left: 0; top: 574px; width: 777px; height: 26px; background: var(--charcoal); color: var(--white); font-size: 8.4px; display: flex; align-items: center; justify-content: flex-end; padding-right: 4px; }

  /* ---------- Inner spread ---------- */
  .about-photo { position: absolute; left: 0; top: 600px; width: 388px; height: 82px;
    background: linear-gradient(90deg, #3a2b28 0%, #6b4a3c 45%, #b89078 80%, #d4b395 100%); }
  .services-photo { position: absolute; left: 0; top: 880px; width: 388px; height: 320px;
    background: linear-gradient(160deg, #2d2d2f 0%, #4a4643 50%, #2a2826 100%); }

  .timeline { position: absolute; width: 3px; background: var(--orange); }
  .timeline.left { left: 15px; top: 655px; height: 545px; }
  .timeline.right { left: 407px; top: 647px; height: 541px; }
  .dot { position: absolute; width: 18px; height: 18px; border-radius: 50%; background: var(--orange); }

  .panel-title { position: absolute; font-family: "Montserrat", sans-serif; font-weight: 800; line-height: 1; }
  .panel-title.big { font-size: 40px; color: var(--white); letter-spacing: -0.5px; }
  .panel-title.about { left: 34px; top: 642px; text-shadow: none; }
  .panel-title.about span.dark { color: var(--white); }
  .panel-title.services { left: 36px; top: 934px; }

  .about-copy { position: absolute; left: 36px; top: 690px; width: 332px; font-size: 10.6px; line-height: 13px; text-align: justify; }
  .about-copy p + p { margin-top: 13px; }

  .services-copy { position: absolute; left: 36px; top: 983px; width: 336px; font-size: 10.6px; line-height: 13px; color: var(--white); }
  .services-copy .lead { margin-bottom: 13px; }
  .package { list-style: none; }
  .package li { position: relative; padding-left: 36px; }
  .package li::before { content: ">"; position: absolute; left: 0; }

  .topic { position: absolute; left: 429px; width: 333px; }
  .topic h2 { font-family: "Montserrat", sans-serif; font-weight: 800; font-size: 28px; line-height: 28px; color: var(--ink); letter-spacing: -0.3px; }
  .topic p { font-size: 8.3px; line-height: 10.6px; text-align: justify; }
  .topic p + p { margin-top: 10.6px; }
</style>
</head>
<body>
<div class="brochure">

  <!-- Outer spread: back panel -->
  <div class="cover-photo" role="img" aria-label="Greyscale photo of smiling international students"></div>

  <svg class="cover-shapes" width="777" height="600" viewBox="0 0 777 600" aria-hidden="true">
    <polygon points="0,528 388,460 388,574 0,574" fill="var(--orange)"/>
    <polygon points="388,278 777,202 777,246 388,320" fill="var(--charcoal)"/>
    <polygon points="388,320 777,246 777,574 388,574" fill="var(--orange)"/>
  </svg>

  <div class="icon-grid">
    <div class="icon-tile" style="left:0;top:0">
      <svg viewBox="0 0 40 40"><polyline points="6,28 20,14 34,28" fill="none" stroke="var(--orange)" stroke-width="6" stroke-linecap="round" stroke-linejoin="round"/></svg>
    </div>
    <div class="icon-tile" style="left:98px;top:0">
      <svg viewBox="0 0 40 40"><path d="M27 5 L35 13 L15 33 L5 35 L7 25 Z" fill="var(--orange)"/></svg>
    </div>
    <div class="icon-tile" style="left:0;top:100px">
      <svg viewBox="0 0 40 40"><circle cx="12" cy="13" r="5" fill="var(--orange)"/><path d="M3 26 a9 8 0 0 1 18 0 Z" fill="var(--orange)"/><circle cx="27" cy="22" r="5" fill="var(--orange)"/><path d="M18 35 a9 8 0 0 1 18 0 Z" fill="var(--orange)"/><path d="M22 6 a8 8 0 0 1 10 6" fill="none" stroke="var(--orange)" stroke-width="2"/><path d="M6 30 a8 8 0 0 0 8 6" fill="none" stroke="var(--orange)" stroke-width="2"/></svg>
    </div>
    <div class="icon-tile" style="left:98px;top:100px">
      <svg viewBox="0 0 40 40"><polygon points="20,9 38,17 20,25 2,17" fill="var(--orange)"/><path d="M10 21 V29 Q20 34 30 29 V21 L20 26 Z" fill="var(--orange)"/></svg>
    </div>
  </div>

  <div class="contact-card">
    <div class="phone-box">
      <svg width="22" height="22" viewBox="0 0 24 24"><path d="M6.6 10.8a15 15 0 0 0 6.6 6.6l2.2-2.2a1 1 0 0 1 1-.25 11.4 11.4 0 0 0 3.6.57 1 1 0 0 1 1 1V20a1 1 0 0 1-1 1A17 17 0 0 1 3 4a1 1 0 0 1 1-1h3.5a1 1 0 0 1 1 1c0 1.25.2 2.45.57 3.57a1 1 0 0 1-.25 1z" fill="none" stroke="var(--white)" stroke-width="1.8"/></svg>
    </div>
    <p>Executive Director &amp; Independent Educational Consultant<br>
      Plorva International Educational Consultants, LLC<br>
      4180 Larkfield Rd<br>
      Suite 12B, Brennick, TX, 75099<br>
      Phone No. : 555-014-2290</p>
  </div>

  <!-- Outer spread: front cover -->
  <div class="brand">
    <div class="brand-dot"></div>
    <div class="brand-name">Plorva International<br>Educational Consultants</div>
  </div>

  <div class="tagline">QUALITY EDUCATION ACCESSIBLE AND AFFORDABLE ACCROSS THE GLOBE.</div>

  <ul class="service-list">
    <li><div class="mini-tile"><svg viewBox="0 0 40 40"><polyline points="6,28 20,14 34,28" fill="none" stroke="var(--white)" stroke-width="5" stroke-linecap="round" stroke-linejoin="round"/></svg></div><span>Boarding Schools</span></li>
    <li><div class="mini-tile"><svg viewBox="0 0 40 40"><path d="M27 5 L35 13 L15 33 L5 35 L7 25 Z" fill="var(--white)"/></svg></div><span>College Admissions</span></li>
    <li><div class="mini-tile"><svg viewBox="0 0 40 40"><circle cx="12" cy="13" r="5" fill="var(--white)"/><path d="M3 26 a9 8 0 0 1 18 0 Z" fill="var(--white)"/><circle cx="27" cy="22" r="5" fill="none" stroke="var(--white)" stroke-width="2"/><path d="M18 35 a9 8 0 0 1 18 0 Z" fill="none" stroke="var(--white)" stroke-width="2"/></svg></div><span>Transfer Students</span></li>
    <li><div class="mini-tile"><svg viewBox="0 0 40 40"><polygon points="20,9 38,17 20,25 2,17" fill="var(--white)"/><path d="M10 21 V29 Q20 34 30 29 V21 L20 26 Z" fill="var(--white)"/></svg></div><span>Graduate Students</span></li>
  </ul>

  <div class="info-bar">Brennick, Texas &nbsp;|&nbsp; +1-555-014-2290 &nbsp;|&nbsp; info@plorvaeducational.example</div>

  <!-- Inner spread: left panel -->
  <div class="about-photo" role="img" aria-label="Photo of students studying together in a library"></div>
  <div class="services-photo" role="img" aria-label="Dark photo of library bookshelves"></div>

  <div class="timeline left"></div>
  <div class="dot" style="left:7px;top:654px"></div>
  <div class="dot" style="left:7px;top:943px"></div>

  <h1 class="panel-title big about">ABOUT US</h1>
  <div class="about-copy">
    <p>Our mission is to make quality education accessible and affordable to the families we serve. Our services are designed with the child's future in mind. Whether one is seeking an academic or non-academic environment, it is important to us that we set our clients up for success.</p>
    <p>We are a family-centered organization and our goals are the same as those of our clients; for their child to thrive and reach their goals and dreams. With over 10 years of experience in the business, we are aware of the financial obstacles created by the ever increasing cost in education. Our expert consultants work closely with families to map out their educational budget and find the best affordable and quality educational options.</p>
  </div>

  <h1 class="panel-title big services">SERVICES</h1>
  <div class="services-copy">
    <p class="lead">Finding the right school or program for your child is one of the most important decisions your family will make. The right choice will make a major impact on your child's future.</p>
    <p>Our package includes:</p>
    <ul class="package">
      <li>Intake interview</li>
      <li>Present range of options based on needs and goals of the family</li>
      <li>Interview coaching</li>
      <li>Assistance with application and essays</li>
      <li>Updates on student progress throughout their enrollment with the school,</li>
      <li>Advisement on financial documents and visa applications</li>
    </ul>
  </div>

  <!-- Inner spread: right panel -->
  <div class="timeline right"></div>
  <div class="dot" style="left:399px;top:642px"></div>
  <div class="dot" style="left:399px;top:767px"></div>
  <div class="dot" style="left:399px;top:945px"></div>
  <div class="dot" style="left:399px;top:1029px"></div>

  <section class="topic" style="top:640px">
    <h2>BOARDING SCHOOLS</h2>
    <p>Students who want the best out of their grade school experience are likely to choose boarding schools because they are proven to better prepare students for university. North American boarding schools provide a quality dynamic experience that will facilitate personal growth in independence, leadership, and confidence as well as provide the academic curriculum necessary to prepare students for university.</p>
  </section>

  <section class="topic" style="top:765px">
    <h2>COLLEGE ADMISSION</h2>
    <p>As Educational Consultants, we specialize in college/university admissions and we understand how confusing, time-consuming, and stressful the application process can be. Our experienced counselors are here to answer your questions and guide you step by step. As Parents and students may have limited access to information on schools, may not know or understand the entire process as a whole, nor where/how to begin, our experts counselors have a solutions.</p>
    <p>Clients increase the odds of admissions with our comprehensive plan of action. We believe that regardless of a student's level of involvement in extra-curricular activities or preparedness, they still possess something they can offer to the university; therefore we help them shine on their college applications.</p>
  </section>

  <section class="topic" style="top:943px">
    <h2>TRANSFER STUDENTS</h2>
    <p>Need to find a school an alternative school that is a better match for you? We work with students and families to transfer from one school to another.</p>
  </section>

  <section class="topic" style="top:1027px">
    <h2>SCHOLARSHIPS</h2>
    <p>Funding the education for your children in some of the world's top schools can be very expensive as tuition and fees increase at an average of 4% every year. We work with you to determine the budget for your family, applying to scholarship available and guide you through the financial aid process.</p>
    <p>Over 70% of our clients have been awarded scholarships or Financial Aid, making your education goals attainable an affordable and your children education possible.</p>
    <p>Include at the bottom of last page "Our consultants are members of NAEP, the leading association for educational consultants in North America."</p>
  </section>

</div>
</body>
</html>
```